Fun, Clean Business Card For Family Focused Travel Agency

I need a business card using specific colors and fonts as in the uploaded files. Ideally, I would like a large image of the logo on the back and all the contact info on the front. Maybe the stars/dots somewhere in a flowy form.

I do want it the contact information to be clear and easy to read. I don't want it to look too busy. Maybe even a bit minimalist.

I plan or ordering the ROUNDED CORNER business cards from Cardwell Press, so please consider that in your design.

Target Market(s)

Families with children, couples, groups of friends

Contact Information for Business Card

Marla Quent, Owner
Marla@TidewayTrips.example
Cell Phone Number 555-218-6034
Office Phone Number 555-647-1295
Specializing in Fablecrest destinations, Goldmere Parkside Resort, Cruises and All-Inclusive Vacations.

Nice but not required:
www.TidewayTrips.example
Facebook, Instagram, Twitter icons with username: TidewayTrips

Font styles to use
Sans Serif

Requirements
Must have
• Please try to use the colors from the logo as much as possible. I understand lighter shades/colors may be needed for some things.
Should not have
• NO SERIF FONTS. That is really the only thing I do not want at all

```html
<!DOCTYPE html>
<html lang="en">
<head>
<meta charset="utf-8">
<title>Tideway Trips – Business Card</title>
<link rel="stylesheet" href="https://fonts.googleapis.com/css2?family=Montserrat:wght@400;500;600;700&display=swap">
<style>
  :root {
    --navy: #161a3a;
    --teal: #14b8a6;
    --teal-light: #1fd0bb;
    --teal-deep: #0e9f8f;
    --white: #ffffff;
    --paper: #f4f4f2;
    --backdrop: #e9ecec;
  }
  * { box-sizing: border-box; margin: 0; padding: 0; }
  html, body { width: 1200px; height: 780px; overflow: hidden; }
  body {
    background: var(--backdrop);
    font-family: "Montserrat", Arial, sans-serif;
    position: relative;
  }

  /* ---------- Front ---------- */
  .card-front {
    position: absolute;
    left: 90px; top: 90px;
    width: 350px; height: 600px;
    border-radius: 24px;
    overflow: hidden;
    background: linear-gradient(180deg, var(--white), var(--paper));
    box-shadow: 0 10px 30px rgba(0,0,0,.18);
  }
  .card-front .shape-layer { position: absolute; inset: 0; }
  .front-brand {
    position: absolute;
    top: 86px; left: 0; right: 0;
    display: flex; align-items: center; justify-content: center; gap: 12px;
  }
  .brand-dot {
    width: 34px; height: 34px; border-radius: 50%;
    background: var(--teal);
    flex: none;
  }
  .brand-name {
    font-weight: 700;
    font-size: 34px;
    color: var(--navy);
    letter-spacing: .5px;
    white-space: nowrap;
  }
  .contact-block {
    position: absolute;
    top: 276px; left: 0; right: 0;
    text-align: center;
    color: var(--white);
  }
  .person-name { font-size: 27px; font-weight: 600; letter-spacing: .5px; line-height: 1.2; }
  .person-role { font-size: 19px; font-weight: 400; color: var(--teal); line-height: 1.2; }
  .contact-row {
    position: relative;
    margin-top: 8px;
    font-size: 17px;
    line-height: 1.25;
    letter-spacing: .4px;
  }
  .contact-row.email { font-size: 14px; letter-spacing: .2px; }
  .row-icon {
    display: flex; align-items: center; justify-content: center;
    margin: 0 auto 4px;
    height: 24px;
    position: relative;
  }
  .row-icon::before, .row-icon::after {
    content: ""; position: absolute; top: 50%;
    width: 90px; height: 1.5px; background: var(--teal);
  }
  .row-icon::before { right: calc(50% + 18px); }
  .row-icon::after { left: calc(50% + 18px); }
  .row-icon svg { width: 24px; height: 24px; }
  .website {
    position: absolute;
    bottom: 24px; left: 0; right: 0;
    text-align: center;
    color: var(--white);
    font-size: 17px; font-weight: 600; letter-spacing: .4px;
  }

  /* ---------- Back ---------- */
  .card-back {
    position: absolute;
    left: 500px; top: 215px;
    width: 600px; height: 350px;
    border-radius: 24px;
    overflow: hidden;
    background: radial-gradient(circle at 62% 38%, var(--teal-light), var(--teal) 55%, var(--teal-deep));
    box-shadow: 0 10px 30px rgba(0,0,0,.18);
    color: var(--white);
  }
  .back-brand {
    position: absolute;
    top: 96px; left: 0; right: 0;
    display: flex; align-items: center; justify-content: center; gap: 18px;
  }
  .back-brand .brand-dot { width: 56px; height: 56px; background: var(--white); }
  .back-brand .brand-name { color: var(--white); font-size: 60px; }
  .tagline {
    position: absolute;
    top: 222px; left: 0; right: 0;
    text-align: center;
    font-size: 17px; line-height: 1.55;
  }
  .tagline strong { font-weight: 700; }
</style>
</head>
<body>

<section class="card-front" aria-label="Business card front">
  <svg class="shape-layer" viewBox="0 0 350 600" preserveAspectRatio="none" aria-hidden="true">
    <path d="M0 222 C 110 200, 250 212, 350 262 L350 600 L0 600 Z" fill="#14b8a6"/>
    <path d="M0 232 C 110 212, 250 226, 350 276 L350 600 L0 600 Z" fill="#161a3a"/>
    <path d="M120 224 C 210 222, 290 240, 340 264" fill="none" stroke="#ffffff" stroke-width="2" stroke-linecap="round"/>
    <rect x="0" y="522" width="350" height="6" fill="#ffffff"/>
    <rect x="0" y="528" width="350" height="72" fill="#14b8a6"/>
  </svg>

  <div class="front-brand">
    <span class="brand-dot"></span>
    <span class="brand-name">Tideway Trips</span>
  </div>

  <div class="contact-block">
    <div class="person-name">Marla Quent</div>
    <div class="person-role">Owner</div>

    <div class="contact-row">
      <div class="row-icon">
        <svg viewBox="0 0 24 24"><circle cx="12" cy="12" r="11" fill="#14b8a6"/><rect x="8.5" y="5.5" width="7" height="13" rx="1.5" fill="none" stroke="#161a3a" stroke-width="1.6"/><circle cx="12" cy="16" r=".9" fill="#161a3a"/></svg>
      </div>
      555-218-6034
    </div>

    <div class="contact-row">
      <div class="row-icon">
        <svg viewBox="0 0 24 24"><circle cx="12" cy="12" r="11" fill="#14b8a6"/><path d="M8 7.5c-1 1 -1 3 1 5.5s4.5 3.5 5.5 2.5l1-1-2-2-1 .8c-1-.5-2.3-1.8-2.8-2.8l.8-1-2-2z" fill="#161a3a"/></svg>
      </div>
      555-647-1295
    </div>

    <div class="contact-row email">
      <div class="row-icon">
        <svg viewBox="0 0 24 24"><circle cx="12" cy="12" r="11" fill="#14b8a6"/><rect x="6.5" y="8" width="11" height="8" rx="1" fill="none" stroke="#161a3a" stroke-width="1.5"/><path d="M6.8 8.4 12 12.4l5.2-4" fill="none" stroke="#161a3a" stroke-width="1.5"/></svg>
      </div>
      Marla@TidewayTrips.example
    </div>
  </div>

  <div class="website">www.TidewayTrips.example</div>
</section>

<section class="card-back" aria-label="Business card back">
  <div class="back-brand">
    <span class="brand-dot"></span>
    <span class="brand-name">Tideway Trips</span>
  </div>
  <p class="tagline">
    <strong>Specializing in</strong> Fablecrest destinations<br>
    Goldmere Parkside Resort | Cruises and All-Inclusive Vacations.
  </p>
</section>

</body>
</html>
```